Podcast Cover Art for Fast Growing Show (Ill include a gracious tip!)

This artwork is for "The Steadfast Fellow Show." The podcast is for men, and it's all about self-improvement, confidence, success, money, women and masculinity. It's for the guy who wants to improve himself. I'd like for my picture to be included — in black and white — and I want the text to read: "The Steadfast Fellow Show" and somewhere in there it'll say: "with Dale Prowen." I'm open to color schemes. The podcast is a little edgy so I'd like for that to be represented in the design. Thank you! (((Here's the podcast page if you wanna check it out: http://steadfastfellowshow.castorbit.net/)))

Target Market(s)

Men who want to attract women and improve their lives!

Font styles to use
Serif

Colors

Designer to choose colors to be used in the design.

Requirements
Must have
• My image in it (in black and white) and the two titles: "The Steadfast Fellow Show" and "with Dale Prowen"
Nice to have
• My logo in it somehow (which is the arrow looking logo attached below). I've also found that my image looks best in black and white and with a circular type cut out (although I'm open to different design ideas). I've attached my logo with a circular cut out below so you can see what I'm talking about.
Should not have
• Flowers. Teddy bears. ice cream.

```html
<!DOCTYPE html>
<html lang="en">
<head>
<meta charset="utf-8">
<title>The Steadfast Fellow Show — Cover Art</title>
<link href="https://fonts.googleapis.com/css2?family=Jost:wght@300;700&display=swap" rel="stylesheet">
<style>
  :root {
    --violet: #3f2a84;
    --plum: #7a1f6e;
    --crimson: #e3122a;
    --halo: #ff2d78;
    --halo-deep: #b02ab0;
    --name-box: #35278a;
    --white: #ffffff;
    --gray-light: #9a9a9a;
    --gray-dark: #2a2a2a;
  }
  html, body {
    margin: 0;
    padding: 0;
    overflow: hidden;
    background: #111;
  }
  .cover {
    position: relative;
    width: 1200px;
    height: 927px;
    overflow: hidden;
    background: linear-gradient(100deg, var(--violet) 0%, var(--plum) 45%, var(--crimson) 100%);
    font-family: "Jost", sans-serif;
    color: var(--white);
  }
  .host-photo {
    position: absolute;
    inset: 0;
  }
  .show-title {
    position: absolute;
    left: 52px;
    top: 28px;
    margin: 0;
    font-weight: 700;
    text-transform: uppercase;
    line-height: 0.82;
    letter-spacing: -1px;
  }
  .show-title .line {
    display: block;
    font-size: 114px;
  }
  .show-title .line-small {
    font-size: 83px;
    margin-top: 6px;
  }
  .brand-mark {
    position: absolute;
    left: 54px;
    top: 800px;
    font-weight: 700;
    font-size: 22px;
    letter-spacing: 2px;
    text-transform: uppercase;
  }
  .host-credit {
    position: absolute;
    left: 763px;
    top: 700px;
  }
  .host-credit .with {
    display: block;
    font-weight: 300;
    font-size: 60px;
    line-height: 1;
    margin: 0 0 4px 14px;
  }
  .host-credit .name {
    display: block;
    width: 415px;
    height: 108px;
    box-sizing: border-box;
    padding-left: 20px;
    background: var(--name-box);
    font-weight: 700;
    font-size: 64px;
    line-height: 108px;
    white-space: nowrap;
  }
</style>
</head>
<body>
<div class="cover">
  <svg class="host-photo" width="1200" height="927" viewBox="0 0 1200 927" role="img" aria-label="Black and white portrait of host Dale Prowen, hands steepled in front of his chin, with a glowing pink cut-out outline">
    <defs>
      <linearGradient id="photo-tone" x1="0" y1="0" x2="0" y2="1">
        <stop offset="0" stop-color="var(--gray-light)"/>
        <stop offset="0.55" stop-color="#6b6b6b"/>
        <stop offset="1" stop-color="var(--gray-dark)"/>
      </linearGradient>
    </defs>
    <path fill="var(--halo-deep)" opacity="0.85"
      d="M448 300 C440 215 510 175 600 178 C700 180 770 230 770 320 L768 470 C768 520 770 560 780 600 C900 615 1060 650 1150 780 L1180 927 L100 927 L150 770 C200 680 330 620 430 600 C425 540 430 470 448 300 Z"/>
    <path fill="var(--halo)"
      d="M430 290 C425 205 495 168 585 170 C685 172 755 222 755 312 L752 465 C752 515 755 555 765 595 C885 610 1045 645 1135 775 L1165 927 L90 927 L138 765 C188 675 318 615 418 595 C412 535 415 465 430 290 Z"/>
    <path fill="url(#photo-tone)"
      d="M445 300 C440 225 505 195 590 196 C680 198 740 240 740 320 L737 465 C737 515 740 550 748 585 C865 605 1020 640 1110 770 L1140 927 L115 927 L160 775 C205 690 330 630 430 610 C428 545 430 470 445 300 Z"/>
  </svg>

  <h1 class="show-title">
    <span class="line">The</span>
    <span class="line">Steadfast</span>
    <span class="line">Fellow</span>
    <span class="line line-small">Show</span>
  </h1>

  <div class="brand-mark">Steadfast</div>

  <div class="host-credit">
    <span class="with">with</span>
    <span class="name">Dale Prowen</span>
  </div>
</div>
</body>
</html>
```